Broschüren-Design für Produzent von hochwertigen Verpackungs- und Präsentationslösungen
Zielgruppe
Wir produzieren hochwertige Verpackungs- und Präsentationslösungen.
Unsere Zielgruppe sind Firmen, welche kreative Premium-Packaging benötigt.
Aufgabenstellung
- Format: A4 hoch
- Umfang: 6 Seiten
- Falzart: Wickelfalz
- Design muss sehr hochwertig sein. Passend zu unseren Produktion (siehe Bilder)
- Wir möchten mit diesem Falzprospekt eine Übersicht über unsere Produkte generieren.
- Die Produkte sind bereits schon hochwertig fotografiert und müssen in einem anspruchsvollen Design in Szene gesetzt werden.
- Der Prospekt sollte die Kunden emotional berühren.
- Auf der Titelseite werden wir den Titel «High Performance Packaging» mit Folien prägen
- Seitenaufbau gemäss meiner Visualisierung (im Anhang)
- Bei jeder Produktkategorie möchte ich ein Grosses Übersichtsbild zusammen mit einem kurzen Text.
Ergänzend können noch weitere (passende) Bilder der jeweiligen Kategorie abgebildet werden.
Im Anhang finden Sie:
- Visualisierung des zu gestaltenden Prospekt
- Werbeflyer (zur Ansicht/Inspiration). In etwa so stellen wir uns das Design/Tonalität vor.
- Weitere passende Produktbilder können vorerst auf der Webseite unseres Produktionspartner (www.bogenhaus.de) entnommen werden.

```html
<!DOCTYPE html>
<html lang="de">
<head>
<meta charset="utf-8">
<title>Produktübersicht – Verpackungs- und Präsentationslösungen</title>
<link rel="stylesheet" href="https://fonts.googleapis.com/css2?family=Playfair+Display:ital,wght@1,900&family=Barlow+Semi+Condensed:wght@300;400&display=swap">
<style>
  :root {
    --navy: #3e4253;
    --paper: #ffffff;
    --panel: #dfe0e6;
    --fold: #e7a9bb;
    --accent: #dc8a55;
    --ink-light: #e6e7ec;
    --ink-dark: #3e4253;
    --body-dark: #4b4f5f;
  }
  * { margin: 0; padding: 0; box-sizing: border-box; }
  html, body { width: 1200px; height: 566px; overflow: hidden; background: var(--paper); }
  .spread { position: relative; width: 1200px; height: 566px; overflow: hidden; background: var(--paper); }
  .band { position: absolute; background: var(--navy); }
  .band--top { left: 0; top: 0; width: 1200px; height: 189px; }
  .band--bottom-left { left: 0; top: 377px; width: 402px; height: 189px; }
  .band--bottom-right { left: 804px; top: 377px; width: 396px; height: 189px; }
  .fold { position: absolute; top: 0; width: 1px; height: 566px; background: var(--fold); opacity: .6; z-index: 5; }
  .fold--one { left: 402px; }
  .fold--two { left: 804px; }

  .product-photo { position: absolute; z-index: 1; border-radius: 2px; }
  .photo--packaging { left: 206px; top: 76px; width: 158px; height: 94px; background: linear-gradient(135deg, #2a2c33, #a08a55 55%, #25262c); }
  .photo--binder { left: 608px; top: 60px; width: 186px; height: 144px; background: linear-gradient(160deg, #d9414f 0 22%, #c9cbd2 22%, #f2f2f4 70%, #b9bbc3); }
  .photo--fan-folder { left: 1049px; top: 24px; width: 108px; height: 173px; background: linear-gradient(180deg, #9b9da3, #6f7177 70%, #4f5157); }
  .photo--slipcase { left: 258px; top: 208px; width: 101px; height: 155px; background: linear-gradient(90deg, #b8bac0 0 40%, #2f3036 40%, #1f2025); }
  .photo--pres-folder { left: 1006px; top: 254px; width: 194px; height: 142px; background: linear-gradient(160deg, #c7c9cf, #eeeef0 55%, #a9abb2); }
  .photo--sample-folder { left: 206px; top: 440px; width: 215px; height: 126px; background: linear-gradient(150deg, #2b2c31, #5a5b60 45%, #b79c86 70%, #e9e9eb); }
  .photo--writing-folder { left: 1008px; top: 430px; width: 192px; height: 136px; background: linear-gradient(150deg, #2d2f3a, #f1f1f3 50%, #d9dadd); }

  .case-panel { position: absolute; left: 440px; top: 227px; width: 326px; height: 301px; background: linear-gradient(180deg, #d9dadf, var(--panel)); z-index: 1; }
  .photo--case { position: absolute; left: 0; top: 0; width: 326px; height: 196px; background: linear-gradient(170deg, #cfd0d5 0%, #f4f4f5 40%, #2f3036 70%, #d9dadf 100%); }

  .category { position: absolute; z-index: 3; white-space: nowrap; }
  .category h2 {
    font-family: "Playfair Display", Georgia, serif;
    font-style: italic; font-weight: 900;
    font-size: 18px; line-height: 1; letter-spacing: .1px;
    margin-bottom: 12px;
  }
  .category p {
    font-family: "Barlow Semi Condensed", "Arial Narrow", sans-serif;
    font-weight: 300; font-size: 9.4px; line-height: 13.45px; letter-spacing: .2px;
  }
  .on-dark h2 { color: #ffffff; }
  .on-dark p { color: var(--ink-light); }
  .on-light h2 { color: var(--ink-dark); }
  .on-light p { color: var(--body-dark); font-weight: 400; }

  .cat--packaging { left: 38px; top: 36px; }
  .cat--binder { left: 440px; top: 36px; }
  .cat--fan-folder { left: 842px; top: 36px; }
  .cat--slipcase { left: 38px; top: 225px; }
  .cat--pres-folder { left: 842px; top: 225px; }
  .cat--sample-folder { left: 38px; top: 414px; }
  .cat--writing-folder { left: 842px; top: 414px; }
  .cat--case { left: 469px; top: 434px; }

  .badge {
    position: absolute; left: 989px; top: 101px; width: 74px; height: 74px; border-radius: 50%;
    background: var(--accent); z-index: 4;
    display: flex; align-items: center; justify-content: center;
  }
  .badge span {
    font-family: "Playfair Display", Georgia, serif; font-style: italic; font-weight: 900;
    font-size: 12px; line-height: 14px; color: var(--navy); text-align: center;
    transform: rotate(-8deg);
  }
</style>
</head>
<body>
<main class="spread">
  <div class="band band--top"></div>
  <div class="band band--bottom-left"></div>
  <div class="band band--bottom-right"></div>
  <div class="fold fold--one"></div>
  <div class="fold fold--two"></div>

  <div class="product-photo photo--packaging" role="img" aria-label="Produktfoto: Premium-Verpackungen in Schwarz und Gold mit Einsatz"></div>
  <div class="product-photo photo--binder" role="img" aria-label="Produktfoto: aufgeschlagener Ringordner mit rotem Einband und Briefbogen"></div>
  <div class="product-photo photo--fan-folder" role="img" aria-label="Produktfoto: graue Fächermappe mit Registern"></div>
  <div class="product-photo photo--slipcase" role="img" aria-label="Produktfoto: schwarzer Schuber mit drei grauen Ordnern"></div>
  <div class="product-photo photo--pres-folder" role="img" aria-label="Produktfoto: geöffnete graue Präsentationsmappe mit Ringmechanik und Stift"></div>
  <div class="product-photo photo--sample-folder" role="img" aria-label="Produktfoto: dunkle Mustermappe mit Holz- und Materialmustern"></div>
  <div class="product-photo photo--writing-folder" role="img" aria-label="Produktfoto: Schreibmappen mit Klemmbrett, Papier und Stift"></div>

  <div class="case-panel">
    <div class="photo--case" role="img" aria-label="Produktfoto: weisser Präsentationskoffer mit Klappdeckel und Produkteinsatz"></div>
  </div>

  <section class="category on-dark cat--packaging">
    <h2>Verpackungen</h2>
    <p>Ma eos magnam nonem estibust laboreium<br>ates alia dolupta speraerum quisti berum<br>explanimil elesedi tatquas.</p>
  </section>
  <section class="category on-dark cat--binder">
    <h2>Ringordner</h2>
    <p>Ma eos magnam nonem estibust laboreium<br>ates alia dolupta speraerum quisti berum<br>explanimil elesedi tatquas.</p>
  </section>
  <section class="category on-dark cat--fan-folder">
    <h2>Fächermappen</h2>
    <p>Ma eos magnam nonem estibust laboreium<br>ates alia dolupta speraerum quisti berum<br>explanimil elesedi tatquas dolupta.</p>
  </section>
  <div class="badge"><span>Exklusiv<br>und hoch-<br>wertig</span></div>

  <section class="category on-light cat--slipcase">
    <h2>Schuber</h2>
    <p>Ma eos magnam nonem estibust laboreium<br>ates alia dolupta speraerum quisti berum<br>explanimil elesedi tatquas. Obit mi, esto<br>doluptis di solent experum et a aut odis alis<br>quibus voluptate plicide rspelectem delitat<br>ibuscipit, in cus eateserae non cor sanim.</p>
  </section>
  <section class="category on-light cat--pres-folder">
    <h2>Präsentationsmappen</h2>
    <p>Ma eos magnam nonem estibust laboreium<br>ates alia dolupta speraerum quisti<br>elesedi magnam.</p>
  </section>
  <section class="category on-light cat--case">
    <h2>Präsentationskoffer</h2>
    <p>Ma eos magnam nonem estibust laboreium ates alia<br>dolupta speraerum quisti berum explanimil elesedi<br>tatquas dolupta speraerum quisti.</p>
  </section>

  <section class="category on-dark cat--sample-folder">
    <h2>Mustermappen</h2>
    <p>Ma eos magnam nonem estibust laboreium<br>ates alia dolupta speraerum quisti<br>explanimil elesedi tatquas.</p>
  </section>
  <section class="category on-dark cat--writing-folder">
    <h2>Schreibmappen</h2>
    <p>Ma eos magnam nonem estibust laboreium<br>ates alia dolupta speraerum quisti<br>explanimil elesedi tatquas.</p>
  </section>
</main>
</body>
</html>
```